Card design for Heating and Cooling company

this is for a heating and cooling company we recently updated our logo and need to update our cards. We attached our logo so you can incorporate it into the card. We specialize in residential and commercial furnace and air condition repairs. Have been in business since 2014.

Phone number 555.284.9137

We need the following phrases
:Repairs, Installations, and maintenance
:Quality work at reasonable prices
:residential/commercial
:Licensed &Insured
:Email Pinegrovehvac47@mailbox-example.com
Name: Teodor K (Ted)
Also on back side I would like my logo with wording :Thank you for your business and refferal

Industry/Entity Type

Hvac

Contact Information for Business Card

:residential/commercial
:Licensed & Insured
Name: Teodor K (Ted)
Number:555.284.9136

Requirements
Must have
• Blue and red colors
Nice to have
• Maybe a pic of a furnace or air conditioner

```html
<!DOCTYPE html>
<html lang="en">
<head>
<meta charset="utf-8">
<title>Pinegrove Heating &amp; Cooling – Business Card</title>
<link href="https://fonts.googleapis.com/css2?family=Roboto:ital,wght@0,400;0,700;1,700&display=swap" rel="stylesheet">
<style>
  :root {
    --brand-blue: #2e3192;
    --brand-red: #ed1c24;
    --wave-red: #ee3b24;
    --paper: #ffffff;
    --backdrop: #e6e7ea;
    --card-shadow: 0 10px 28px rgba(20, 22, 40, 0.18);
  }
  * { box-sizing: border-box; margin: 0; padding: 0; }
  html, body {
    width: 1200px; height: 900px; overflow: hidden;
    background: var(--backdrop);
    font-family: "Roboto", Arial, sans-serif;
  }
  .sheet {
    width: 1200px; height: 900px;
    display: flex; flex-direction: column; align-items: center; justify-content: center;
    gap: 50px;
  }
  .card {
    position: relative;
    width: 700px; height: 400px;
    background: var(--paper);
    box-shadow: var(--card-shadow);
    overflow: hidden;
  }
  .card__waves { position: absolute; inset: 0; width: 100%; height: 100%; }

  /* Front */
  .front__icon { position: absolute; left: 232px; top: 46px; width: 96px; height: 80px; }
  .front__details { position: absolute; left: 290px; top: 140px; color: var(--brand-blue); }
  .front__name { font-size: 30px; font-weight: 700; color: var(--brand-red); margin-bottom: 22px; }
  .front__nickname { color: var(--brand-blue); }
  .contact-row { display: flex; align-items: flex-start; gap: 10px; font-size: 17px; line-height: 24px; }
  .contact-row + .contact-row { margin-top: 2px; }
  .contact-row__icon { width: 16px; height: 16px; margin-top: 4px; flex: none; }
  .contact-row__lines { display: flex; flex-direction: column; }

  /* Back */
  .back__brand {
    position: absolute; right: 60px; top: 96px;
    display: flex; align-items: center; gap: 12px;
  }
  .back__brand-dot { width: 26px; height: 26px; border-radius: 50%; background: var(--brand-blue); }
  .back__brand-name { font-size: 30px; font-weight: 700; color: var(--brand-blue); letter-spacing: 1px; line-height: 1.05; }
  .back__brand-name small { display: block; font-size: 15px; letter-spacing: 3px; }
  .back__thanks {
    position: absolute; left: 330px; top: 232px; width: 340px;
    font-size: 22px; font-weight: 700; font-style: italic; color: var(--brand-red); line-height: 1.3;
  }
</style>
</head>
<body>
<main class="sheet">

  <section class="card card--front" aria-label="Card front">
    <svg class="card__waves" viewBox="0 0 700 400" preserveAspectRatio="none" aria-hidden="true">
      <path fill="var(--wave-red)" d="M0,0 H215 C150,120 190,290 95,400 H0 Z"/>
      <path fill="var(--brand-blue)" d="M0,0 H120 C150,140 90,250 55,400 H0 Z"/>
    </svg>

    <svg class="front__icon" viewBox="0 0 96 80" aria-label="Air conditioner icon" role="img">
      <g fill="none" stroke="var(--brand-blue)" stroke-width="3" stroke-linecap="round" stroke-linejoin="round">
        <rect x="4" y="6" width="88" height="36" rx="4"/>
        <line x1="14" y1="32" x2="82" y2="32"/>
        <line x1="74" y1="16" x2="82" y2="16"/>
        <path d="M28,52 c-4,5 4,9 0,16"/>
        <path d="M40,52 c-4,5 4,9 0,16"/>
        <path d="M52,52 c-4,5 4,9 0,16"/>
      </g>
    </svg>

    <div class="front__details">
      <h1 class="front__name">Teodor K <span class="front__nickname">(Ted)</span></h1>

      <div class="contact-row">
        <svg class="contact-row__icon" viewBox="0 0 16 16" aria-hidden="true">
          <path fill="var(--brand-red)" d="M3.5,1 L6,1.5 L6.8,5 L5,6.2 C5.8,8 7.8,10 9.8,11 L11,9.2 L14.5,10 L15,12.5 C14,14.5 12,15.2 10,14.4 C5.8,12.8 3.2,10.2 1.6,6 C0.8,4 1.5,2 3.5,1 Z"/>
        </svg>
        <span>555.284.9136</span>
      </div>

      <div class="contact-row">
        <svg class="contact-row__icon" viewBox="0 0 16 16" aria-hidden="true">
          <rect x="0.5" y="2.5" width="15" height="11" fill="var(--brand-red)"/>
          <path d="M1,3 L8,9 L15,3" fill="none" stroke="#fff" stroke-width="1.4"/>
        </svg>
        <span>Pinegrovehvac47@mailbox-example.com</span>
      </div>

      <div class="contact-row">
        <svg class="contact-row__icon" viewBox="0 0 16 16" aria-hidden="true">
          <circle cx="9" cy="2.5" r="2" fill="var(--brand-red)"/>
          <path d="M6,6 H10 L8,14 H10" fill="none" stroke="var(--brand-red)" stroke-width="2.4" stroke-linecap="round"/>
        </svg>
        <span class="contact-row__lines">
          <span>Repairs, Installations, and maintenance</span>
          <span>Quality work at reasonable prices</span>
          <span>residential/commercial</span>
          <span>Licensed &amp; Insured</span>
        </span>
      </div>
    </div>
  </section>

  <section class="card card--back" aria-label="Card back">
    <svg class="card__waves" viewBox="0 0 700 400" preserveAspectRatio="none" aria-hidden="true">
      <path fill="var(--brand-blue)" d="M0,0 H270 C250,230 420,370 700,400 H0 Z"/>
      <path fill="var(--brand-red)" d="M0,0 H270 C262,60 262,110 276,165 C190,110 110,80 0,70 Z"/>
    </svg>

    <div class="back__brand">
      <span class="back__brand-dot" aria-hidden="true"></span>
      <p class="back__brand-name">PINEGROVE<small>HEATING &amp; COOLING</small></p>
    </div>

    <p class="back__thanks">Thank you for your business and referral</p>
  </section>

</main>
</body>
</html>
```